Engineering Consultant Business Card

I'm starting a new business as a high-end engineering consultant in a niche field. I've attached the jpg for my logo plus the branding guideline document that I've been following. You can see my business website here: www.tarvikworks.com
I'd like a business card that has the logo on one side, then the other side has (in any order): Tarvik Works, Inc.
Dana Whitlock
President and Chief EMC Engineer
www.tarvikworks.com
dana@tarvikworks.com
Optional: motto "We will solve your EMC problems as early as possible—ideally before they even start."
I'm not planning on including a phone number
Target Market(s)
Businesses, especially makers of electronics hardware
Industry/Entity Type
Electrical engineering
Contact Information for Business Card
Company name, my name, website, email

```html
<!DOCTYPE html>
<html lang="en">
<head>
<meta charset="utf-8">
<title>Tarvik Works, Inc. – Business Card</title>
<link href="https://fonts.googleapis.com/css2?family=Montserrat:wght@400;700&display=swap" rel="stylesheet">
<style>
  :root {
    --brand-blue: #2c48a0;
    --brand-blue-deep: #1f3688;
    --ink: #3a3a3a;
    --card: #f6f6f6;
    --backdrop: #d9dadc;
  }
  * { box-sizing: border-box; margin: 0; padding: 0; }
  html, body { width: 1200px; height: 1200px; overflow: hidden; }
  body {
    background: var(--backdrop);
    font-family: "Montserrat", sans-serif;
    position: relative;
  }
  .card {
    position: absolute;
    left: 220px;
    width: 760px;
    height: 434px;
    background: linear-gradient(135deg, #ffffff 0%, var(--card) 60%, #ececec 100%);
    overflow: hidden;
    box-shadow: 0 10px 30px rgba(0,0,0,.18);
  }
  .card--front { top: 110px; }
  .card--back { top: 650px; }

  /* Front */
  .wordmark {
    position: absolute;
    left: 0; right: 0; top: 150px;
    display: flex; align-items: center; justify-content: center; gap: 18px;
    color: var(--brand-blue);
    font-weight: 700;
    font-size: 54px;
    letter-spacing: 1px;
  }
  .wordmark__dot {
    width: 34px; height: 34px; border-radius: 50%;
    background: var(--brand-blue);
  }
  .front-band {
    position: absolute; left: 0; right: 0; bottom: 0; height: 16px;
    background: var(--brand-blue);
  }
  .front-tab {
    position: absolute; left: 340px; right: 0; bottom: 0; height: 70px;
    background: linear-gradient(90deg, #3f5cb0, var(--brand-blue));
    border-top-left-radius: 34px;
    display: flex; align-items: center; justify-content: flex-end;
    padding-right: 70px;
    color: #ffffff;
    font-size: 22px;
    letter-spacing: .5px;
  }

  /* Back */
  .identity { position: absolute; left: 70px; top: 60px; }
  .identity__name {
    color: var(--brand-blue);
    font-weight: 700;
    font-size: 36px;
    letter-spacing: .5px;
  }
  .identity__title {
    color: var(--ink);
    font-size: 20px;
    margin-top: 6px;
  }
  .contact {
    position: absolute; left: 70px; top: 270px;
    color: var(--ink);
    font-size: 19px;
    line-height: 32px;
  }
  .contact__row { display: flex; align-items: center; gap: 10px; }
  .contact__icon { width: 16px; height: 16px; fill: var(--brand-blue); flex: none; }
  .corner-accent {
    position: absolute; right: -120px; bottom: -170px;
    width: 440px; height: 440px; border-radius: 50%;
    background: linear-gradient(180deg, #3a57ad, var(--brand-blue-deep));
  }
</style>
</head>
<body>

<section class="card card--front" aria-label="Business card front">
  <div class="wordmark"><span class="wordmark__dot"></span>Tarvik Works</div>
  <div class="front-band"></div>
  <div class="front-tab">Tarvik Works, Inc.</div>
</section>

<section class="card card--back" aria-label="Business card back">
  <div class="identity">
    <h1 class="identity__name">Dana Whitlock</h1>
    <p class="identity__title">President and chief EMC Engineer</p>
  </div>

  <div class="contact">
    <p class="contact__row">
      <svg class="contact__icon" viewBox="0 0 16 16" aria-hidden="true"><path d="M1 3h14v10H1z M1 3l7 5.5L15 3" stroke="#fff" stroke-width="1.2"/></svg>
      dana@tarvikworks.com
    </p>
    <p class="contact__row">
      <svg class="contact__icon" viewBox="0 0 16 16" aria-hidden="true"><circle cx="8" cy="8" r="7"/><path d="M1 8h14M8 1c-3 3.5-3 10.5 0 14M8 1c3 3.5 3 10.5 0 14" stroke="#fff" stroke-width="1" fill="none"/></svg>
      www.tarvikworks.com
    </p>
  </div>

  <div class="corner-accent"></div>
</section>

</body>
</html>
```